ALDER DENTAL *

Target Market(s)

Adults 18-60

Contact Information for Business Card

Website: alderdentalvlm.com
Phone number 555 304 2796 email: crestdentalvlm@mailbox-example.com
Address:471 S. Holloway rd
Suite#24, TX70000
Dr. Marcus Telfer, DDS

Font styles to use
Sans Serif

Requirements
Must have
• Logo, phone number website, doctor,
• 's name

```html
<!DOCTYPE html>
<html lang="en">
<head>
<meta charset="utf-8">
<title>Alder Dental – Business Card</title>
<link href="https://fonts.googleapis.com/css2?family=Work+Sans:wght@300;400;500&display=swap" rel="stylesheet">
<style>
  :root {
    --bg: #dcdcdc;
    --navy: #131c30;
    --teal: #1b8aa0;
    --ink: #3a3d44;
    --rule: #5a5d63;
    --white: #ffffff;
  }
  * { margin: 0; padding: 0; box-sizing: border-box; }
  html, body { width: 1200px; height: 930px; overflow: hidden; background: var(--bg); }
  body { position: relative; font-family: "Work Sans", sans-serif; color: var(--ink); }

  .card {
    position: absolute;
    width: 640px; height: 366px;
    border-radius: 26px;
    overflow: hidden;
    box-shadow: 0 6px 18px rgba(0,0,0,0.18);
  }

  /* Front */
  .card-front { left: 90px; top: 60px; background: var(--navy); }
  .card-front .brand {
    position: absolute; left: 0; right: 0; top: 82px;
    display: flex; flex-direction: column; align-items: center; gap: 22px;
  }
  .brand-dot {
    width: 96px; height: 96px; border-radius: 50%;
    border: 2px solid var(--white);
  }
  .card-front .brand-name {
    font-weight: 300; font-size: 50px; letter-spacing: 2px; color: var(--white);
  }

  /* Back */
  .card-back { left: 470px; top: 480px; background: var(--white); }
  .card-back .shapes { position: absolute; inset: 0; }
  .back-tab { position: absolute; left: 90px; top: 0; width: 84px; height: 58px; background: var(--navy); }
  .back-dot {
    position: absolute; left: 92px; top: 30px;
    width: 80px; height: 80px; border-radius: 50%;
    background: var(--white); border: 2px solid var(--rule);
  }
  .back-brand {
    position: absolute; left: 88px; top: 122px;
    font-weight: 300; font-size: 40px; letter-spacing: 1.5px; color: var(--ink);
  }

  .doctor { position: absolute; right: 40px; top: 48px; text-align: right; }
  .doctor-name {
    font-weight: 500; font-size: 26px; color: var(--teal); letter-spacing: 0.5px;
  }
  .doctor-rule { width: 330px; margin-left: auto; margin-top: 4px; border-top: 1px solid var(--rule); }
  .doctor-title { font-size: 13px; color: var(--ink); margin-top: 3px; letter-spacing: 1px; }

  .address {
    position: absolute; right: 40px; top: 140px; text-align: right;
    font-size: 15px; line-height: 1.4; letter-spacing: 0.5px;
  }

  .divider { position: absolute; left: 100px; top: 196px; width: 250px; border-top: 1px solid var(--rule); }

  .contacts { position: absolute; left: 100px; top: 208px; list-style: none; font-size: 16px; line-height: 1.45; letter-spacing: 0.5px; }
  .contacts li { display: flex; align-items: center; gap: 8px; }
  .contacts svg { width: 12px; height: 12px; fill: none; stroke: var(--teal); stroke-width: 1.6; flex: none; }
  .contacts .accent { color: var(--teal); }
</style>
</head>
<body>

  <section class="card card-front" aria-label="Card front">
    <div class="brand">
      <span class="brand-dot"></span>
      <span class="brand-name">ALDER DENTAL</span>
    </div>
  </section>

  <section class="card card-back" aria-label="Card back">
    <svg class="shapes" viewBox="0 0 640 366" preserveAspectRatio="none" aria-hidden="true">
      <path d="M250 366 L440 318 C480 306 490 266 535 262 L640 262 L640 366 Z" fill="var(--navy)"/>
      <path d="M0 358 L425 306" stroke="var(--teal)" stroke-width="5" fill="none"/>
    </svg>

    <div class="back-tab"></div>
    <div class="back-dot"></div>
    <div class="back-brand">ALDER DENTAL</div>

    <div class="doctor">
      <div class="doctor-name">DR. MARCUS TELFER</div>
      <div class="doctor-rule"></div>
      <div class="doctor-title">DDS</div>
    </div>

    <div class="address">471 S. HOLLOWAY RD<br>Larkston, TX70000</div>

    <div class="divider"></div>

    <ul class="contacts">
      <li><svg viewBox="0 0 12 12"><path d="M3 1 L5 4 L4 5 C5 7 6 8 7 8 L8 7 L11 9 L10 11 C5 11 1 7 1 2 Z"/></svg><span>555 304 2796</span></li>
      <li><svg viewBox="0 0 12 12"><rect x="1" y="3" width="10" height="7"/><path d="M1 3 L6 7 L11 3"/></svg><span>info@alderdentalvlm.com</span></li>
      <li><svg viewBox="0 0 12 12"><circle cx="6" cy="6" r="5"/><path d="M1 6 H11 M6 1 C3 4 3 8 6 11 M6 1 C9 4 9 8 6 11"/></svg><span>www.<span class="accent">alderdentalvlm</span>.com</span></li>
    </ul>
  </section>

</body>
</html>
```